Creation of a Velmaro Flyer design

As part of the cr% 26 # 233; ation of our soci% 26 # 233; t% 26 # 233 ;, we wish to cr% 26 # 233; er a flyer pr% 26 # 233; feeling our diff% 26 # 233; annuities% 26 # 233; s business advisory services% 26 # 233; foreign% 26 # 232; res who wish to develop their activities% 26 # 233; s in Switzerland. We want a double-sided flyer that presents% 26 # 233; society% 26 # 233; t% 26 # 233; d% 26 # 39; a c% 26 # 244; t% 26 # 233; and who presents% 26 # 233; benefits of the other. We have d% 26 # 233; j% 26 # 224; made a very basic provisional flyer to be able to present our activities. We put it to you as an example.

Target Market(s)

European companies% 26 # 233; internal% 26 # 233; res% 26 # 233; es by the market% 26 # 233; Swiss

Industry/Entity Type

Business Consultant

Colors

Designer to choose colors to be used in the design.

Requirements
Must have
• Company name and contact details
A field to detail the services
Nice to have
• Some% 26 # 233; l% 26 # 233; elements that recall Switzerland and some% 26 # 233; l% 26 # 233; elements that recall c% 26 # 244; t% 26 # 233; % 26quot; business% 26quot;

```html
<!DOCTYPE html>
<html lang="en">
<head>
<meta charset="utf-8">
<title>Velmaro Flyer</title>
<link href="https://fonts.googleapis.com/css2?family=Open+Sans:ital,wght@0,400;0,600;0,700;1,600&display=swap" rel="stylesheet">
<style>
:root{
  --backdrop:#6b6b6b;
  --navy:#1d3c55;
  --navy-deep:#163247;
  --band-top:#2a4e6c;
  --band-bottom:#1c3a52;
  --paper:#ffffff;
  --ink:#2b2b2b;
  --white:#ffffff;
}
*{box-sizing:border-box;margin:0;padding:0}
html,body{width:1200px;height:1200px;overflow:hidden;background:var(--backdrop)}
body{position:relative;font-family:"Open Sans",Arial,sans-serif;color:var(--ink)}
.page{position:absolute;top:218px;width:544px;height:764px;background:var(--paper);overflow:hidden}
.page--front{left:38px}
.page--back{left:618px}
.top-band{position:absolute;left:0;top:0;width:100%;height:16px;background:var(--navy)}

/* front header */
.brand{position:absolute;left:16px;top:34px;display:flex;align-items:center;gap:16px}
.brand__square{width:34px;height:34px;border-radius:6px;background:var(--navy)}
.brand__name{font-size:27px;font-weight:400;letter-spacing:3px;color:var(--navy);text-transform:uppercase}
.office{position:absolute;right:20px;top:25px;text-align:right;font-size:10.4px;line-height:12px;color:var(--ink)}
.office__title{font-weight:700;color:var(--navy);font-size:11px;margin-bottom:2px}

.photo{position:absolute;left:0;width:100%}
.photo--castle{top:86px;height:350px;background:linear-gradient(180deg,#3f8fe0 0%,#7fb4e8 25%,#b48a6a 45%,#8a6a50 62%,#2fb0b2 75%,#1f9fa8 100%)}
.photo--bridge{top:16px;height:232px;background:linear-gradient(180deg,#5aa4ea 0%,#a9c9e8 30%,#b06a3a 48%,#9a5a32 65%,#4f7a9a 82%,#2f5f80 100%)}
.photo--alps{top:420px;height:292px;background:linear-gradient(180deg,rgba(255,255,255,0) 0%,#dde9f4 35%,#c4d6e8 60%,#8a8c8e 82%,#8a6a3a 100%)}

.intro-band{position:absolute;left:0;top:436px;width:100%;height:110px;background:linear-gradient(180deg,var(--band-top),var(--band-bottom));color:var(--white);padding:18px 19px 0}
.intro-band__text{font-size:10px;line-height:11.8px;font-weight:600;text-align:justify}
.intro-band__tagline{margin-top:12px;font-size:10px;line-height:12px;font-style:italic;font-weight:600;text-align:center}

.columns{position:absolute;top:572px;left:18px;right:18px;display:flex;gap:24px;font-size:10.2px;line-height:11.9px;text-align:justify}
.columns__col{flex:1}
.columns__col p+p{margin-top:9px}

/* back */
.headline-band{position:absolute;left:0;top:248px;width:100%;height:72px;background:linear-gradient(180deg,var(--band-top),var(--band-bottom));color:var(--white);padding:14px 24px 0;font-size:13px;line-height:15px;font-weight:700;letter-spacing:.4px;text-transform:uppercase}
.lead{position:absolute;left:17px;right:17px;top:334px;font-size:10.2px;line-height:12px;font-weight:600;color:#111}
.services{position:absolute;top:380px;left:28px;right:18px;display:flex;gap:26px;font-size:10.2px;line-height:11.9px}
.services__col{flex:1;list-style:none}
.services__col:first-child{flex:0 0 236px;text-align:justify}
.services__item{position:relative;padding-left:16px;margin-bottom:7px}
.services__item svg{position:absolute;left:0;top:1px}
.services__note{padding-left:16px;margin-bottom:7px}

/* footer */
.footer{position:absolute;left:0;top:704px;width:100%;height:50px}
.footer__bar{position:absolute;left:69px;right:0;top:8px;height:32px;background:var(--navy);display:flex;align-items:center;color:var(--white);font-size:10.4px}
.footer__item{display:flex;align-items:center;gap:6px;position:absolute;top:9px}
.footer__sep{position:absolute;top:7px;width:2px;height:18px;background:var(--white)}
.footer__mark{position:absolute;left:16px;top:0;width:48px;height:48px;border-radius:9px;background:var(--navy);border:2px solid var(--white);box-shadow:0 0 0 1px var(--navy);display:flex;align-items:center;justify-content:center;color:var(--white);font-size:8.5px;font-weight:600}
</style>
</head>
<body>

<section class="page page--front">
  <div class="top-band"></div>
  <header>
    <div class="brand"><div class="brand__square"></div><div class="brand__name">Velmaro</div></div>
    <div class="office">
      <div class="office__title">Neuchâtel Office</div>
      <div>Velmaro Sàrl</div>
      <div>Rue des Tilleuls 4 <b>|</b> 2017 Boudry (Neuchâtel)</div>
    </div>
  </header>
  <div class="photo photo--castle" role="img" aria-label="Lakeside Swiss castle with turrets and turquoise water under a blue sky"></div>
  <div class="intro-band">
    <p class="intro-band__text">The potential of the Swiss market offers many business opportunities to foreign companies, however there are some tariff and non-tariff barriers to cope with, such as its strong requirements in terms of quality and innovation, cultural and linguistic differences, specific rules applied to certain products or services.</p>
    <p class="intro-band__tagline">Velmaro is there to support you<br>in your administrative and strategic procedures!</p>
  </div>
  <div class="columns">
    <div class="columns__col">
      <p>Velmaro strives to deepen the understanding of your business and acts as your local partner. We assist you in defining together all the services that best meet your needs.</p>
      <p>Our consulting skills are focused on high added value sectors, such as food and beverages, fashion &amp; lifestyle, products and services for leading industries (pharmaceutical, chemical, precision mechanics) or sustainable solutions (renewable energies, recyclable materials).</p>
    </div>
    <div class="columns__col">
      <p>From our office in Neuchâtel* and with our language knowledges, we are able to cover the whole of Switzerland. Having many years of experience in economic promotion and business management, we are familiar with the Swiss trade and foreign companies wishing to export to Switzerland.</p>
      <p style="margin-top:14px">*as of August 2020, we will open an office in Zurich as well</p>
    </div>
  </div>
  <footer class="footer">
    <div class="footer__bar">
      <span class="footer__item" style="left:13px"><svg width="10" height="16" viewBox="0 0 10 16"><path d="M3 1 L5 1 L6 4 L4 5 Q4 9 6 11 L8 10 L9 13 L7 15 Q1 13 1 4 Z" fill="none" stroke="#fff" stroke-width="1.2"/></svg>+41 (0)32 555 01 23</span>
      <span class="footer__sep" style="left:150px"></span>
      <span class="footer__item" style="left:181px"><svg width="18" height="12" viewBox="0 0 18 12"><rect x="1" y="1" width="16" height="10" fill="none" stroke="#fff"/><path d="M1 1 L9 7 L17 1" fill="none" stroke="#fff"/></svg>info@velmaro.ch</span>
      <span class="footer__sep" style="left:318px"></span>
      <span class="footer__item" style="left:351px"><svg width="14" height="14" viewBox="0 0 14 14"><circle cx="7" cy="7" r="6" fill="none" stroke="#fff"/><ellipse cx="7" cy="7" rx="2.6" ry="6" fill="none" stroke="#fff"/><path d="M1 7 H13 M2 4 H12 M2 10 H12" stroke="#fff" stroke-width=".8"/></svg>www.velmaro.ch</span>
    </div>
    <div class="footer__mark">Velmaro</div>
  </footer>
</section>

<section class="page page--back">
  <div class="top-band"></div>
  <div class="photo photo--alps" role="img" aria-label="Snow-capped Alpine peak above a mountain range"></div>
  <div class="photo photo--bridge" role="img" aria-label="Wooden covered bridge with flower boxes and a stone water tower on a lake"></div>
  <div class="headline-band">You are convinced of the potential of your product or service and you wish to focus on the Swiss market, or you want to expand your market share!</div>
  <p class="lead">Thanks to its personalized approach and tailor-made assistance, Velmaro offers you the right support to develop your business activities and answers to all your questions about the swiss market. As a partner we assist you in finding market opportunities:</p>
  <div class="services">
    <ul class="services__col">
      <li class="services__item"><svg width="11" height="11" viewBox="0 0 11 11"><rect width="11" height="11" rx="2" fill="#1d3c55"/><path d="M2.5 5.5 L4.6 7.6 L8.6 3.2" fill="none" stroke="#fff" stroke-width="1.5"/></svg>By providing commercial contacts that match your target profiles;</li>
      <li class="services__item"><svg width="11" height="11" viewBox="0 0 11 11"><rect width="11" height="11" rx="2" fill="#1d3c55"/><path d="M2.5 5.5 L4.6 7.6 L8.6 3.2" fill="none" stroke="#fff" stroke-width="1.5"/></svg>By listing the legal and regulatory requirements specific to the Swiss market (Switzerland is not an EU member State);</li>
      <li class="services__item"><svg width="11" height="11" viewBox="0 0 11 11"><rect width="11" height="11" rx="2" fill="#1d3c55"/><path d="M2.5 5.5 L4.6 7.6 L8.6 3.2" fill="none" stroke="#fff" stroke-width="1.5"/></svg>By putting you in contact with private or public interlocutors in the context of an individual contact programme;</li>
      <li class="services__item"><svg width="11" height="11" viewBox="0 0 11 11"><rect width="11" height="11" rx="2" fill="#1d3c55"/><path d="M2.5 5.5 L4.6 7.6 L8.6 3.2" fill="none" stroke="#fff" stroke-width="1.5"/></svg>By preparing a market study that measures the potential of your product or service;</li>
      <li class="services__item"><svg width="11" height="11" viewBox="0 0 11 11"><rect width="11" height="11" rx="2" fill="#1d3c55"/><path d="M2.5 5.5 L4.6 7.6 L8.6 3.2" fill="none" stroke="#fff" stroke-width="1.5"/></svg>By adapting your marketing material (website, brochures, flyers, etc.) to the specific needs of the Swiss market and by translating it into German and/or French;</li>
    </ul>
    <ul class="services__col">
      <li class="services__item"><svg width="11" height="11" viewBox="0 0 11 11"><rect width="11" height="11" rx="2" fill="#1d3c55"/><path d="M2.5 5.5 L4.6 7.6 L8.6 3.2" fill="none" stroke="#fff" stroke-width="1.5"/></svg>By organizing a promotional event that is tailored to your needs;</li>
      <li class="services__item"><svg width="11" height="11" viewBox="0 0 11 11"><rect width="11" height="11" rx="2" fill="#1d3c55"/><path d="M2.5 5.5 L4.6 7.6 L8.6 3.2" fill="none" stroke="#fff" stroke-width="1.5"/></svg>By representing you at trade shows or fairs;</li>
      <li class="services__note">By assuming the fiscal representation of your company;</li>
      <li class="services__item"><svg width="11" height="11" viewBox="0 0 11 11"><rect width="11" height="11" rx="2" fill="#1d3c55"/><path d="M2.5 5.5 L4.6 7.6 L8.6 3.2" fill="none" stroke="#fff" stroke-width="1.5"/></svg>By offering you logistical and administrative support.</li>
    </ul>
  </div>
  <footer class="footer">
    <div class="footer__bar">
      <span class="footer__item" style="left:13px"><svg width="10" height="16" viewBox="0 0 10 16"><path d="M3 1 L5 1 L6 4 L4 5 Q4 9 6 11 L8 10 L9 13 L7 15 Q1 13 1 4 Z" fill="none" stroke="#fff" stroke-width="1.2"/></svg>+41 (0)32 555 01 23</span>
      <span class="footer__sep" style="left:150px"></span>
      <span class="footer__item" style="left:181px"><svg width="18" height="12" viewBox="0 0 18 12"><rect x="1" y="1" width="16" height="10" fill="none" stroke="#fff"/><path d="M1 1 L9 7 L17 1" fill="none" stroke="#fff"/></svg>info@velmaro.ch</span>
      <span class="footer__sep" style="left:318px"></span>
      <span class="footer__item" style="left:351px"><svg width="14" height="14" viewBox="0 0 14 14"><circle cx="7" cy="7" r="6" fill="none" stroke="#fff"/><ellipse cx="7" cy="7" rx="2.6" ry="6" fill="none" stroke="#fff"/><path d="M1 7 H13 M2 4 H12 M2 10 H12" stroke="#fff" stroke-width=".8"/></svg>www.velmaro.ch</span>
    </div>
    <div class="footer__mark">Velmaro</div>
  </footer>
</section>

</body>
</html>
```